Inspiration Poster

Inspirational Poster that has a Kamran Dulo like abstract look (http://www.vexalo.com/images/search?q=kamran+dulo&FORM=HDRSC2) with the text:

"we walk not in order to arrive at the promise land but because walking itself is a revolution"
-Peter Ambrick

```html
<!DOCTYPE html>
<html lang="en">
<head>
<meta charset="utf-8">
<title>We Walk — Inspiration Poster</title>
<link rel="stylesheet" href="https://fonts.googleapis.com/css2?family=Economica:wght@400;700&display=swap">
<style>
  :root {
    --ink: #050608;
    --paper: #f7fbfd;
    --cyan: #1fb4e6;
    --blue: #1666b8;
    --deep: #0b2a55;
    --sky: #bfe6f6;
    --lilac: #b9a9d8;
    --plum: #5a4a82;
    --amber: #b98a3c;
  }
  * { margin: 0; padding: 0; box-sizing: border-box; }
  html, body {
    width: 849px;
    height: 1200px;
    overflow: hidden;
    background: var(--paper);
  }
  .poster {
    position: relative;
    width: 849px;
    height: 1200px;
    overflow: hidden;
    font-family: "Economica", "Arial Narrow", sans-serif;
    color: var(--ink);
  }
  .crowd-photo {
    position: absolute;
    inset: 0;
    background:
      radial-gradient(ellipse 180px 520px at 250px 700px, rgba(11,42,85,0.55), transparent 70%),
      radial-gradient(ellipse 140px 480px at 60px 720px, rgba(11,42,85,0.6), transparent 70%),
      radial-gradient(ellipse 130px 420px at 740px 640px, rgba(40,30,70,0.55), transparent 70%),
      radial-gradient(ellipse 240px 200px at 820px 1150px, rgba(185,138,60,0.7), transparent 70%),
      radial-gradient(ellipse 260px 240px at 60px 1150px, rgba(11,42,85,0.75), transparent 70%),
      radial-gradient(ellipse 420px 700px at 520px 520px, rgba(255,255,255,0.95), transparent 75%),
      linear-gradient(90deg, var(--blue) 0%, var(--cyan) 14%, var(--sky) 34%, var(--paper) 55%, #e9e6f3 75%, var(--lilac) 90%, var(--plum) 100%);
  }
  .quote {
    position: absolute;
    left: 328px;
    top: 0;
  }
  .quote-line {
    position: absolute;
    left: 0;
    white-space: nowrap;
    font-size: 72px;
    font-weight: 400;
    line-height: 1;
    letter-spacing: 0.5px;
  }
  .quote-line.l1 { top: 283px; }
  .quote-line.l2 { top: 387px; }
  .quote-line.l3 { top: 491px; }
  .quote-line.l4 { top: 596px; }
  .quote-line.l5 { top: 699px; }
  .quote-line.l6 { top: 803px; }
  .quote-line.finale {
    top: 893px;
    font-size: 118px;
    letter-spacing: 1px;
  }
  .attribution {
    position: absolute;
    right: 136px;
    top: 1032px;
    font-size: 30px;
    white-space: nowrap;
  }
</style>
</head>
<body>
  <main class="poster">
    <div class="crowd-photo" role="img" aria-label="Motion-blurred photograph of people walking through a bright hall, in cyan, blue and lilac tones"></div>

    <blockquote class="quote">
      <p class="quote-line l1">We Walk</p>
      <p class="quote-line l2">Not In Order</p>
      <p class="quote-line l3">To Arrive At</p>
      <p class="quote-line l4">The Promise Land</p>
      <p class="quote-line l5">But Because</p>
      <p class="quote-line l6">Walking Itself Is</p>
      <p class="quote-line finale">A Revolution.</p>
    </blockquote>

    <p class="attribution">– Peter Ambrick</p>
  </main>
</body>
</html>
```